Banner Set for a Gay Dating Site

We need animated banners sized 300x250, 300x600, 970x250, 338x235 and 928x244.

Each banner should display 4-6 different men.

Sloagn: "Meet great guys from your area"

A call-to-action-button saying "Register now!"

The logo should be placed on the banner.

Data format: GIF

The banner should be very eye-catching. The banner will be used for the site www.mosspilot.net

The banner will be used on sites with lots of videos and there they have to be noticed somehow. And mostly the background on these sites is black.

You can use the attaches images. No stock photos allowed.

Men 18-99 yo

Dating

• Animated Subjects
• Rainbows

```html
<!DOCTYPE html>
<html lang="en">
<head>
<meta charset="utf-8">
<title>Moss Pilot – Banner Set</title>
<link rel="stylesheet" href="https://fonts.googleapis.com/css2?family=Antonio:wght@600&family=Raleway:wght@500;600;700&display=swap">
<style>
:root{
  --stage:#939598;
  --gold:#a68a3e;
  --white:#ffffff;
  --cream:#f3ece0;
  --ink:#111111;
  --skin-light:#e3b99a;
  --skin-mid:#c99676;
  --skin-deep:#a87558;
  --wall-warm:#f2dfb8;
  --wall-cool:#e6e6e6;
  --wall-grey:#cfcfcf;
  --foliage:#4f6a3a;
  --denim:#4d6a92;
  --dark-top:#2b2b2b;
  --pink-shirt:#e8ccd4;
  --kitchen:#b8b0a4;
  --party:#6fc6b8;
}
*{margin:0;padding:0;box-sizing:border-box}
html,body{width:893px;height:1200px;overflow:hidden;background:var(--stage)}
body{position:relative;font-family:"Raleway",sans-serif}
.size-label{position:absolute;color:var(--white);font-weight:700;font-size:18px;letter-spacing:.5px}
.banner{position:absolute;overflow:hidden}
.abs{position:absolute}
.photo{position:absolute}
.photo.round{border-radius:50%}
.tone-foliage{background:linear-gradient(180deg,var(--foliage) 0%,var(--skin-light) 45%,var(--dark-top) 100%)}
.tone-harness-warm{background:linear-gradient(180deg,var(--wall-warm) 0%,var(--skin-mid) 50%,var(--denim) 100%)}
.tone-towel{background:linear-gradient(180deg,var(--wall-grey) 0%,var(--skin-light) 45%,var(--white) 100%)}
.tone-pink-shirt{background:linear-gradient(90deg,var(--wall-warm) 0%,var(--pink-shirt) 45%,var(--skin-mid) 70%,var(--denim) 100%)}
.tone-white-tank{background:linear-gradient(180deg,var(--wall-cool) 0%,var(--skin-light) 40%,var(--white) 65%,var(--skin-mid) 100%)}
.tone-dark-tank{background:linear-gradient(180deg,var(--wall-cool) 0%,var(--skin-mid) 50%,var(--dark-top) 100%)}
.tone-harness-black{background:linear-gradient(90deg,var(--wall-grey) 0%,var(--skin-deep) 35%,var(--dark-top) 50%,var(--skin-deep) 65%,var(--wall-grey) 100%)}
.tone-kitchen{background:linear-gradient(180deg,var(--kitchen) 0%,var(--skin-light) 45%,var(--denim) 100%)}
.tone-red-brief{background:linear-gradient(180deg,var(--white) 0%,var(--skin-mid) 45%,#d0322e 62%,var(--skin-light) 100%)}
.tone-party{background:linear-gradient(135deg,var(--party) 0%,var(--skin-light) 45%,var(--skin-deep) 100%)}
.cta{position:absolute;background:var(--gold);color:var(--white);font-weight:700;display:flex;align-items:center;justify-content:center;letter-spacing:.4px;white-space:nowrap}
.brand{position:absolute;display:flex;align-items:center;gap:5px;color:var(--gold);font-family:"Antonio",sans-serif;font-weight:600;letter-spacing:1px;white-space:nowrap}
.brand .dot{border-radius:50%;background:var(--gold);flex:none}
.headline-condensed{position:absolute;font-family:"Antonio",sans-serif;font-weight:600;line-height:1.15;white-space:nowrap}
</style>
</head>
<body>

<!-- 970x250 -->
<div class="size-label" style="left:77px;top:64px">970X250</div>
<div class="banner" style="left:78px;top:101px;width:783px;height:202px;background:var(--white)">
  <div class="brand" style="left:78px;top:40px;font-size:22px"><span class="dot" style="width:13px;height:13px"></span>MOSS PILOT</div>
  <div class="abs" style="left:0;top:116px;width:269px;text-align:center;font-weight:700;font-size:29px;line-height:1.2;color:var(--ink)">MEET GREAT<br>GUYS FROM</div>
  <div class="photo tone-foliage" style="left:269px;top:0;width:102px;height:202px" role="img" aria-label="Young man outdoors in front of foliage"></div>
  <div class="photo tone-harness-warm" style="left:371px;top:0;width:106px;height:202px" role="img" aria-label="Man in harness seated against a warm wall"></div>
  <div class="photo tone-towel" style="left:477px;top:0;width:102px;height:202px" role="img" aria-label="Smiling young man with a towel"></div>
  <div class="photo tone-pink-shirt" style="left:579px;top:0;width:104px;height:202px" role="img" aria-label="Man opening a pink shirt"></div>
  <div class="photo tone-white-tank" style="left:683px;top:0;width:100px;height:202px" role="img" aria-label="Young man in a white tank top"></div>
  <div class="cta" style="left:413px;top:133px;width:217px;height:54px;font-size:22px">REGISTER NOW!</div>
</div>

<!-- 928x244 -->
<div class="size-label" style="left:78px;top:338px">928X244</div>
<div class="banner" style="left:80px;top:372px;width:749px;height:197px;background:var(--cream)">
  <div class="photo tone-kitchen round" style="left:14px;top:16px;width:113px;height:113px" role="img" aria-label="Young man seated in a kitchen"></div>
  <div class="photo tone-red-brief round" style="left:136px;top:16px;width:113px;height:113px" role="img" aria-label="Young man in red briefs on a stool"></div>
  <div class="photo tone-pink-shirt round" style="left:259px;top:16px;width:113px;height:113px" role="img" aria-label="Man opening a pink shirt"></div>
  <div class="headline-condensed" style="left:387px;top:18px;font-size:27px;color:var(--ink)">MEET GREAT GUYS FROM YOUR AREA</div>
  <div class="photo tone-party round" style="left:383px;top:72px;width:113px;height:113px" role="img" aria-label="Smiling young man against a colourful backdrop"></div>
  <div class="photo tone-dark-tank round" style="left:505px;top:72px;width:113px;height:113px" role="img" aria-label="Man in a dark tank top"></div>
  <div class="photo tone-harness-black round" style="left:629px;top:72px;width:113px;height:113px" role="img" aria-label="Young man in a black harness"></div>
  <div class="brand" style="left:26px;top:153px;font-size:15px"><span class="dot" style="width:9px;height:9px"></span>MOSS PILOT</div>
  <div class="cta" style="left:132px;top:145px;width:171px;height:40px;font-size:16px">REGISTER NOW!</div>
</div>

<!-- 300x600 -->
<div class="size-label" style="left:79px;top:610px">300X600</div>
<div class="banner" style="left:78px;top:641px;width:242px;height:484px;background:var(--white)">
  <div class="abs" style="left:0;top:0;width:242px;height:131px;background:var(--gold)"></div>
  <div class="headline-condensed" style="left:10px;top:20px;font-size:25px;color:var(--white);line-height:1.2">MEET GREAT GUYS<br>FROM YOUR AREA</div>
  <div class="cta" style="left:11px;top:85px;width:150px;height:36px;font-size:15px;background:var(--white);color:var(--gold)">REGISTER NOW!</div>
  <div class="photo tone-kitchen" style="left:0;top:133px;width:121px;height:184px" role="img" aria-label="Young man seated in a kitchen"></div>
  <div class="photo tone-red-brief" style="left:121px;top:133px;width:121px;height:184px" role="img" aria-label="Young man in red briefs on a stool"></div>
  <div class="photo tone-harness-warm" style="left:0;top:317px;width:121px;height:167px" role="img" aria-label="Man in harness seated against a warm wall"></div>
  <div class="photo tone-party" style="left:121px;top:317px;width:121px;height:167px" role="img" aria-label="Smiling young man against a colourful backdrop"></div>
  <div class="abs" style="left:72px;top:264px;width:96px;height:96px;border-radius:50%;background:var(--white);display:flex;align-items:center;justify-content:center">
    <div class="brand" style="position:static;font-size:14px">MOSS PILOT</div>
  </div>
</div>

<!-- 300x250 -->
<div class="size-label" style="left:359px;top:610px">300X250</div>
<div class="banner" style="left:359px;top:641px;width:242px;height:202px;background:var(--white)">
  <div class="brand" style="left:10px;top:22px;font-size:14px"><span class="dot" style="width:8px;height:8px"></span>MOSS PILOT</div>
  <div class="cta" style="left:8px;top:63px;width:103px;height:26px;font-size:11px">REGISTER NOW!</div>
  <div class="abs" style="left:128px;top:15px;font-size:16px;line-height:1.5;color:var(--ink);font-weight:500">MEET GREAT<br>GUYS FROM<br>YOUR AREA</div>
  <div class="photo tone-dark-tank" style="left:0;top:97px;width:60px;height:105px" role="img" aria-label="Man in a dark tank top"></div>
  <div class="photo tone-harness-black" style="left:60px;top:97px;width:69px;height:105px" role="img" aria-label="Young man in a black harness"></div>
  <div class="photo tone-white-tank" style="left:129px;top:97px;width:66px;height:105px" role="img" aria-label="Young man in a white tank top"></div>
  <div class="photo tone-harness-warm" style="left:195px;top:97px;width:47px;height:105px" role="img" aria-label="Man in harness seated against a warm wall"></div>
</div>

<!-- 338x235 -->
<div class="size-label" style="left:359px;top:875px">338X235</div>
<div class="banner" style="left:359px;top:905px;width:273px;height:190px;background:var(--white)">
  <div class="headline-condensed" style="left:8px;top:6px;font-size:20px;color:var(--gold)">MEET GREAT GUYS FROM YOUR AREA</div>
  <div class="brand" style="left:10px;top:45px;font-size:13px"><span class="dot" style="width:8px;height:8px"></span>MOSS PILOT</div>
  <div class="cta" style="left:112px;top:36px;width:148px;height:35px;font-size:14px">REGISTER NOW!</div>
  <div class="photo tone-dark-tank" style="left:0;top:81px;width:70px;height:109px" role="img" aria-label="Man in a dark tank top"></div>
  <div class="photo tone-harness-black" style="left:70px;top:81px;width:74px;height:109px" role="img" aria-label="Young man in a black harness"></div>
  <div class="photo tone-white-tank" style="left:144px;top:81px;width:68px;height:109px" role="img" aria-label="Young man in a white tank top"></div>
  <div class="photo tone-harness-warm" style="left:212px;top:81px;width:61px;height:109px" role="img" aria-label="Man in harness seated against a warm wall"></div>
</div>

</body>
</html>
```